Loaf Harbor The Next Generation

we have a website www.loafharbor.ae which needs a complete graphical overhaul.
We are a bakery in Dubai, producing artisan breads and related products. Also salads and sandwiches. All fresh, all handmade, best quality.
We'd like to have something that looks fresh, modern, nice colours (no dark colours). Trendy but still transporting the feeling of the "good ol' bakery).
Our customers are expats, mostly english speakers. But we'd like to attract more different nationalities!
Also, customers are individuals and also companies (offices, airlines, yacht charters...) The third section are coffee shops, restaurants, hotels....
We have also an online shop. This is a MUST and can be optimised.
We'd like to stick with wordpress and woocommerce.
It MUST be responsive and easy to navigate on mobile devices. 60% of our customers order on mobile phones... browsing is even more.

Industry/Entity Type

Bakery

```html
<!DOCTYPE html>
<html lang="en">
<head>
<meta charset="utf-8">
<title>Loaf Harbor Bakery</title>
<link href="https://fonts.googleapis.com/css2?family=Open+Sans:ital,wght@0,400;0,600;0,700;0,800;1,400&display=swap" rel="stylesheet">
<style>
:root{
  --green:#3d5c2b;
  --green-dark:#2f4a20;
  --brown:#6b4a22;
  --ink:#222;
  --muted:#666;
  --line:#ddd;
  --paper:#fff;
  --footer:#f6f6f4;
}
*{box-sizing:border-box;margin:0;padding:0}
html,body{width:1200px;height:3482px;overflow:hidden}
body{font-family:"Open Sans",Arial,sans-serif;color:var(--ink);background:var(--paper);position:relative}
.abs{position:absolute}
.topbar{left:0;top:0;width:1200px;height:24px;background:var(--green);color:#fff;font-size:11px;display:flex;align-items:center;justify-content:space-between;padding:0 97px}
.topbar span{margin-right:26px}
.topbar .right span{margin:0 0 0 24px}
.header{left:0;top:24px;width:1200px;height:169px}
.brand{position:absolute;left:97px;top:60px;width:161px;height:80px;border:2px solid var(--brown);display:flex;align-items:center;justify-content:center;gap:8px;font-weight:800;font-size:20px;color:var(--green)}
.brand i{width:12px;height:12px;background:var(--brown);display:block}
.nav a{position:absolute;top:90px;font-size:12.5px;color:#333;text-decoration:none;letter-spacing:.2px}
.nav a.active{color:var(--green);font-weight:600}
.cart{position:absolute;left:1062px;top:80px;width:36px;height:36px;border:1px solid var(--line);border-radius:50%;display:flex;align-items:center;justify-content:center}

/* photo areas: soft layered gradients in the picture's main tones */
.hero{left:0;top:193px;width:1200px;height:517px;background:
  radial-gradient(ellipse 330px 260px at 960px 380px,#efe6d8 0%,#d9cab2 45%,rgba(200,180,150,0) 75%),
  radial-gradient(ellipse 200px 110px at 1090px 120px,#b27a3e 0%,rgba(150,100,50,0) 80%),
  radial-gradient(ellipse 420px 220px at 260px 110px,#d9aa5c 0%,#b98440 35%,rgba(120,80,40,0) 75%),
  radial-gradient(ellipse 520px 200px at 420px 460px,#8a5a2e 0%,rgba(90,55,25,0) 80%),
  linear-gradient(100deg,#4d321a 0%,#6e4a27 40%,#8b6438 65%,#5c3e20 100%)}
.hero::after{content:"";position:absolute;inset:0;background:rgba(0,0,0,.12)}
.hero h1{position:absolute;z-index:1;left:0;width:1200px;top:115px;text-align:center;color:#fff;font-size:78px;font-weight:800;line-height:93px;text-transform:uppercase;letter-spacing:1px;text-shadow:0 2px 8px rgba(0,0,0,.35)}
.btn-hero{position:absolute;z-index:1;left:525px;top:336px;width:150px;height:44px;border:2px solid #fff;color:#fff;font-size:13px;font-weight:600;display:flex;align-items:center;justify-content:center}
.dots{position:absolute;z-index:1;top:462px;left:553px;display:flex;gap:11px}
.dots b{width:12px;height:12px;border-radius:50%;background:#fff;display:block}
.dots b.on{background:var(--green)}

.tile{top:754px;width:311px;height:212px;border-bottom:5px solid var(--green)}
.tile .band{position:absolute;left:0;top:80px;width:100%;height:39px;background:rgba(255,255,255,.8);display:flex;align-items:center;justify-content:center;font-size:15px;font-weight:700;color:var(--green)}
.rule{left:97px;width:1003px;height:1px;background:var(--line)}
.section-title{font-size:30px;font-weight:600;letter-spacing:.5px}
.menu-card .label{position:absolute;left:0;bottom:0;width:311px;height:46px;background:rgba(61,92,43,.92);color:#fff;font-size:14px;font-weight:700;display:flex;align-items:center;justify-content:space-between;padding:0 22px}
.prod{top:1908px;width:230px}
.prod .pic{height:244px;position:relative}
.zoom{position:absolute;right:0;bottom:0;width:46px;height:46px;background:rgba(0,0,0,.35);display:flex;align-items:center;justify-content:center}
.prod h3{margin-top:37px;font-size:12.5px;font-weight:600;text-transform:uppercase}
.prod .price{margin-top:14px;color:var(--green);font-size:13px;font-weight:600}
.prod p{margin-top:12px;font-size:11.5px;color:var(--muted);line-height:18px}
.prod .add{margin-top:20px;width:102px;height:40px;background:var(--green);color:#fff;font-size:11.5px;display:flex;align-items:center;justify-content:center}
.arrow-btn{top:1838px;width:28px;height:28px;border:1px solid var(--line);border-radius:50%;display:flex;align-items:center;justify-content:center}
.testimonial{left:0;top:2421px;width:1200px;height:318px;color:#fff;background:
  radial-gradient(ellipse 260px 90px at 520px 30px,#c23a22 0%,rgba(160,50,30,0) 80%),
  radial-gradient(ellipse 300px 120px at 180px 40px,#8ea04a 0%,rgba(100,120,50,0) 80%),
  radial-gradient(ellipse 320px 140px at 980px 60px,#9aa94c 0%,rgba(110,120,50,0) 80%),
  radial-gradient(ellipse 360px 150px at 700px 250px,#c79f86 0%,rgba(170,120,100,0) 80%),
  radial-gradient(ellipse 260px 160px at 1120px 260px,#b9b5a8 0%,rgba(150,150,140,0) 80%),
  linear-gradient(100deg,#4a4326,#6b5330 45%,#6f6038 70%,#4b4528)}
.testimonial::after{content:"";position:absolute;inset:0;background:rgba(20,20,10,.45)}
.testimonial > *{z-index:1}
.avatar{position:absolute;left:135px;top:86px;width:144px;height:144px;border-radius:50%;background:radial-gradient(circle at 50% 40%,#f3e6dc,#d9b8a6 70%,#c99a88);border:5px solid #fff}
.testimonial blockquote{position:absolute;left:309px;top:96px;width:760px;font-style:italic;font-size:12.5px;line-height:29px}
.testimonial cite{position:absolute;left:309px;top:197px;font-style:normal;font-weight:700;font-size:15px}
.feature{top:2820px;width:316px;height:174px;border:1px solid var(--line);text-align:center}
.feature h4{margin-top:14px;font-size:14px;font-weight:600}
.feature p{margin-top:10px;font-size:12.5px;color:var(--muted)}
.feature svg{margin-top:36px}
.footer{left:0;top:3101px;width:1200px;height:334px;background:var(--footer);border-top:4px solid var(--green)}
.footer h5{position:absolute;top:73px;font-size:16px;font-weight:600;letter-spacing:.5px}
.footer ul{position:absolute;top:122px;list-style:none;font-size:12.5px;color:#444}
.footer li{height:31px}
.footer li::before{content:"»";color:var(--green);margin-right:14px}
.footer .about{position:absolute;left:95px;top:114px;width:295px;font-size:12.5px;line-height:26px;color:#444}
.social{position:absolute;left:95px;top:232px;display:flex;gap:7px}
.social b{width:26px;height:26px;border:1px solid #777;border-radius:50%;display:block}
.news p{position:absolute;left:817px;top:112px;width:290px;font-size:11.5px;line-height:22px;color:#444}
.email{position:absolute;left:817px;top:162px;width:265px;height:40px;border:1px solid var(--line);background:#fff;font-size:12px;color:#777;display:flex;align-items:center;justify-content:space-between;padding:0 16px 0 20px}
.subscribe{position:absolute;left:817px;top:220px;width:108px;height:38px;background:var(--brown);color:#fff;font-size:12px;display:flex;align-items:center;justify-content:center}
.bottombar{left:0;top:3435px;width:1200px;height:47px;background:var(--green);color:#fff;font-size:12px;display:flex;align-items:center;padding:0 97px}
.cards{position:absolute;right:97px;top:13px;display:flex;gap:4px}
.cards b{width:24px;height:18px;background:#fff;border-radius:2px;display:block}
</style>
</head>
<body>

<div class="abs topbar">
  <div><span>☎ CALL US : 050 000 12 34</span><span>✉ MAIL US : orders@loafharbor.ae</span></div>
  <div class="right"><span>♥ MY WISHLIST</span><span>● SIGN IN</span></div>
</div>

<header class="abs header">
  <div class="brand"><i></i>Loaf Harbor</div>
  <nav class="nav">
    <a class="active" style="left:355px">WELCOME</a>
    <a style="left:448px">OUR MENU</a>
    <a style="left:545px">OUR BOXES</a>
    <a style="left:648px">GREAT BRITISH PIES</a>
    <a style="left:792px">ORDER AND DELIVERY</a>
    <a style="left:949px">GET IN TOUCH</a>
  </nav>
  <div class="cart"><svg width="14" height="14" viewBox="0 0 14 14"><path d="M1 2h2l2 7h6l2-5H4" fill="none" stroke="#3d5c2b" stroke-width="1.5"/><circle cx="6" cy="12" r="1.2" fill="#3d5c2b"/><circle cx="11" cy="12" r="1.2" fill="#3d5c2b"/></svg></div>
</header>

<section class="abs hero" role="img" aria-label="Wheat ears and a wooden scoop of flour on a rustic table">
  <h1>Loaf Harbor<br>Bakery</h1>
  <div class="btn-hero">SHOP NOW</div>
  <div class="dots"><b class="on"></b><b></b><b></b><b></b><b></b></div>
</section>

<div class="abs tile" style="left:97px;background:radial-gradient(ellipse 170px 120px at 50% 60%,#e9bd6c,#c98f3c 60%,rgba(160,60,50,0) 95%),linear-gradient(160deg,#d9d3c8,#b04a3a 70%,#8a2f2a)" role="img" aria-label="Baked pie with lattice crust"><div class="band">ABOUT US</div></div>
<div class="abs tile" style="left:443px;background:radial-gradient(ellipse 90px 60px at 25% 22%,#b5461f,#8a3518 60%,rgba(200,190,170,0) 90%),radial-gradient(ellipse 120px 80px at 80% 25%,#e4b25a,rgba(200,150,60,0) 85%),radial-gradient(ellipse 200px 90px at 55% 95%,#a06a3a,rgba(120,80,40,0) 85%),linear-gradient(#d8cfc0,#6e4a2e)" role="img" aria-label="British pie with baked beans and greens"><div class="band">GREAT BRITISH PIES</div></div>
<div class="abs tile" style="left:791px;background:radial-gradient(ellipse 110px 60px at 30% 20%,#e8c270,rgba(220,170,80,0) 85%),radial-gradient(ellipse 120px 70px at 75% 25%,#d59c44,rgba(200,140,60,0) 85%),radial-gradient(ellipse 200px 90px at 50% 92%,#e0a95e,rgba(200,140,70,0) 85%),linear-gradient(#b98a4a,#c98a45)" role="img" aria-label="Golden baked pastries"><div class="band">ORDER AND DELIVERY</div></div>

<div class="abs rule" style="top:1014px"></div>

<h2 class="abs section-title" style="left:0;width:1200px;top:1076px;text-align:center">OUR MENU</h2>

<div class="abs menu-card" style="left:97px;top:1165px;width:490px;height:246px;background:radial-gradient(ellipse 160px 110px at 25% 35%,#e9dcc0,rgba(220,210,180,0) 85%),radial-gradient(ellipse 140px 90px at 60% 60%,#d8c7a2,rgba(200,180,150,0) 85%),radial-gradient(ellipse 120px 70px at 40% 80%,#7f9a4d,rgba(110,140,70,0) 85%),linear-gradient(90deg,#5d6a4a 0%,#8a8c6e 60%,#2d2f2a 78%,#b8c2cc 80%,#d6dde2 100%)" role="img" aria-label="Tray of sandwich platters">
  <div class="label">SANDWICH PLATTERS <span>➜</span></div>
</div>
<div class="abs menu-card" style="left:97px;top:1439px;width:490px;height:246px;background:radial-gradient(ellipse 90px 60px at 15% 30%,#e7a864,rgba(220,150,90,0) 85%),radial-gradient(ellipse 90px 60px at 45% 25%,#dd9a58,rgba(210,140,80,0) 85%),radial-gradient(ellipse 90px 60px at 80% 35%,#d98e50,rgba(200,130,70,0) 85%),radial-gradient(ellipse 220px 70px at 50% 70%,#6f7f3c,rgba(100,110,60,0) 85%),linear-gradient(#e6ddd6,#c9955e 60%,#e8e2dc)" role="img" aria-label="Mini burger rolls as finger food">
  <div class="label">FINGER FOODS <span>➜</span></div>
</div>
<div class="abs menu-card" style="left:613px;top:1165px;width:487px;height:520px;background:radial-gradient(ellipse 120px 110px at 30% 30%,#a7521e,#8b3f14 50%,rgba(140,100,70,0) 95%),radial-gradient(ellipse 120px 110px at 70% 30%,#a7521e,#8b3f14 50%,rgba(140,100,70,0) 95%),radial-gradient(ellipse 160px 170px at 50% 70%,#b0602a,#86401a 45%,rgba(140,100,70,0) 90%),linear-gradient(#a19a90,#8d8378 50%,#a8a195)" role="img" aria-label="Heart-shaped braided loaf on wooden boards">
  <div class="label" style="top:235px;bottom:auto;width:487px;justify-content:center">BREADS, BAPS AND MORE</div>
</div>

<div class="abs rule" style="top:1764px;left:0;width:1200px"></div>

<h2 class="abs section-title" style="left:97px;top:1830px;font-size:28px">FEATURED PRODUCTS</h2>
<div class="abs arrow-btn" style="left:1030px">‹</div>
<div class="abs arrow-btn" style="left:1068px">›</div>

<div class="abs prod" style="left:97px">
  <div class="pic" style="background:radial-gradient(ellipse 90px 60px at 30% 25%,#c7c58a,rgba(180,180,120,0) 85%),radial-gradient(ellipse 110px 80px at 55% 80%,#b7b46f,rgba(160,160,90,0) 85%),linear-gradient(135deg,#7d8e45,#a5a667 50%,#6e8338)" role="img" aria-label="Steak and potato pie with fries">
    <div class="zoom"><svg width="22" height="22" viewBox="0 0 22 22"><circle cx="9" cy="9" r="7" fill="none" stroke="#fff" stroke-width="2.5"/><path d="M14 14l6 6M6 9h6M9 6v6" stroke="#fff" stroke-width="2.5"/></svg></div>
  </div>
  <h3>Steak and Potato Pie, Round</h3>
  <div class="price">15.00 AED</div>
  <p>Best topside beef, trimmed and cut into cubes and sautéed ...</p>
  <div class="add">ADD TO CART</div>
</div>
<div class="abs prod" style="left:355px">
  <div class="pic" style="background:radial-gradient(ellipse 60px 50px at 30% 70%,#f0d7b0,rgba(230,200,160,0) 85%),radial-gradient(ellipse 60px 50px at 70% 75%,#e7c49a,rgba(220,180,140,0) 85%),radial-gradient(ellipse 70px 60px at 65% 25%,#a86b34,rgba(150,90,40,0) 85%),linear-gradient(#5a3a22,#c99b68 55%,#e8d0ac)" role="img" aria-label="Assorted bread loaves and rolls"></div>
  <h3>Couples Box</h3>
  <div class="price">90.00 AED</div>
  <p>This box contains 1 small brown sliced loaf 1 small white sliced loaf...</p>
  <div class="add">ADD TO CART</div>
</div>
<div class="abs prod" style="left:613px">
  <div class="pic" style="background:radial-gradient(ellipse 60px 45px at 25% 25%,#d8b27a,rgba(210,170,110,0) 85%),radial-gradient(ellipse 70px 55px at 40% 70%,#dba35a,rgba(210,150,80,0) 85%),radial-gradient(ellipse 50px 40px at 85% 25%,#8a2a1c,rgba(130,40,30,0) 85%),linear-gradient(#7b5a3a,#a88256 50%,#c49a62)" role="img" aria-label="Mini pies on a plate"></div>
  <h3>Mini Pies (20pcs)</h3>
  <div class="price">140.00 AED</div>
  <p>Our set of 20 pies include: 5 Steak and Mushroom mini pies...</p>
  <div class="add">ADD TO CART</div>
</div>
<div class="abs prod" style="left:870px">
  <div class="pic" style="background:radial-gradient(ellipse 40px 30px at 50% 40%,#c9321f,rgba(200,50,30,0) 85%),radial-gradient(ellipse 90px 80px at 50% 50%,#86a449,rgba(120,150,70,0) 80%),radial-gradient(ellipse 120px 120px at 50% 50%,#e4d6bd,rgba(220,200,170,0) 90%),linear-gradient(#4a4a3a,#8c8064)" role="img" aria-label="Platter of sandwich triangles"></div>
  <h3>Classic Cut</h3>
  <div class="price">95.00 AED – 115.00 AED</div>
  <p>The platter has 24 triangles or slices and includes Chicken &amp; Stuffing...</p>
  <div class="add">ADD TO CART</div>
</div>

<section class="abs testimonial" role="img" aria-label="Close-up of a sandwich with lettuce and tomato in the background">
  <div class="avatar" role="img" aria-label="Customer portrait"></div>
  <blockquote>“Sed ut perspiciatis unde omnis iste natus error sit voluptatem accusantium doloremque laudantium, totam rem aperiam, eaque ipsa quae ab illo inventore veritatis et quasi architecto beatae vitae dicta sunt explicabo. Nemo enim ipsam voluptatem quia voluptas sit aspernatur aut odit aut fugit, sed quia consequuntur magni dolores eos qui ratione voluptatem sequi nesciunt.”</blockquote>
  <cite>- INVENTOREITATIS</cite>
  <div class="abs" style="left:795px;top:196px;font-size:18px;font-weight:600">‹ ›</div>
  <div class="abs" style="left:990px;top:182px;font-size:52px;font-weight:800;line-height:52px">”</div>
</section>

<div class="abs feature" style="left:97px">
  <svg width="40" height="40" viewBox="0 0 40 40"><path d="M36 4 4 18l13 5 5 13z M17 23 36 4" fill="none" stroke="#3d5c2b" stroke-width="2.5" stroke-linejoin="round"/></svg>
  <h4>FREE SHIPPING</h4><p>on all order over $200.00</p>
</div>
<div class="abs feature" style="left:441px">
  <svg width="40" height="40" viewBox="0 0 40 40"><path d="M6 15h8l16-9v28l-16-9H6z M12 25l3 10h5l-3-10" fill="#3d5c2b"/></svg>
  <h4>FRIENDLY SUPPORT</h4><p>24 hours per day, excluding holiday</p>
</div>
<div class="abs feature" style="left:785px">
  <svg width="40" height="40" viewBox="0 0 40 40"><path d="M9 12A14 14 0 1 1 7 24" fill="none" stroke="#3d5c2b" stroke-width="4"/><path d="M3 6l8 0-2 9z" fill="#3d5c2b"/><path d="M20 12v9l6 4" fill="none" stroke="#3d5c2b" stroke-width="3"/></svg>
  <h4>MONEY BACK</h4><p>10 days for free return and exchange</p>
</div>

<footer class="abs footer">
  <h5 style="left:95px">KEEP IN TOUCH</h5>
  <p class="about">Are you searching for great bread? Maybe a mouth-watering sandwich? Is your next party coming up and you need finger food? No, you're looking for this great platters!</p>
  <div class="social"><b></b><b></b><b></b><b></b></div>

  <h5 style="left:432px">MY ACCOUNT</h5>
  <ul style="left:432px"><li>Policies</li><li>Orders</li><li>Return</li><li>Bulk Discount</li><li>Quality</li></ul>

  <h5 style="left:627px">QUICK LINKS</h5>
  <ul style="left:627px"><li>Request Quote</li><li>Information</li><li>Phone &amp; Mail</li><li>Privacy</li><li>Terms of Use</li></ul>

  <h5 style="left:817px">NEWSLETTER</h5>
  <div class="news"><p>Signup to be the first who receive our latest news and promotions</p></div>
  <div class="email">Your email <span>✉</span></div>
  <div class="subscribe">SUBSCRIBE</div>
</footer>

<div class="abs bottombar">Copyright © Loaf Harbor Bakery2017. All rights reserved.
  <div class="cards"><b></b><b></b><b></b><b></b></div>
</div>

</body>
</html>
```